Honey Label Design (145 × 55 mm) – Premium / Minimal Style

Project Description
I am looking for a professional label design for a 500 g honey jar (twist-off, copper-colored lid).
The design should look premium, elegant, and minimal, reflecting natural quality and regional authenticity.
I expect two design proposals from each designer:

One concept based strictly on my color and style guidelines
One completely free creative concept (designer's own interpretation)

⚠️ Important: The layout and positioning of all elements must follow my specifications exactly (see below). Creativity is welcome in style, colors, and typography—but not in layout structure and content.

Label Size and Constraints

Final size: 145 mm × 55 mm (landscape)
All elements must remain fully within the label area
No part (especially the hexagon) may extend beyond the label boundaries

Design Style

Minimal, clean, premium
No clutter, no excessive colors
Preferred colors:

Warm natural tones (honey, beige, brown)
Inspired by the branding of: www.wabenhaus-laden. de
Subtle copper tone accents (to match the lid)

Background

Very subtle illustrated/sketched background
Motif:

Wildflower meadow (foreground)
Mixed forest (background)

Style should be fine line / sketch style, not photorealistic
The background must remain very soft so text remains clearly readable

Central Element (Mandatory)

A hexagon (honeycomb shape) centered on the label
Inside text:

“GERMAN HONEY”
“500 g”

The hexagon must be:

Fully inside the label (no overlapping, my example is wrong)
Visually balanced and centered

Left Text Block (Important)
The following content (in german) must be placed left-aligned (not centered!):
Bottling point:
Lutz Pfeiffer Beekeeping
Obere Lindmarkweg 17
08437 Wabental
Tel.: 04521 5522417
mail@wabenhaus-laden.de
Typography must be clean and clearly structured.

Mandatory White Fields (Very Important)
There must be exactly 3 white boxes:
Size:

Each: 28 mm × 12 mm
No visible border

Positioning (must follow exactly):

Bottom center

Completely blank (for honey type)

Right side – upper field

Text above: “Best before:”

Right side – lower field (directly below)

Text above: “Lot number”

⚠️ All three fields must:

Be identical in size
Be perfectly aligned
Match the layout shown in the reference image

Layout Rules (Strict)

The arrangement of elements is fixed and must not be changed
Center field must be directly below the hexagon
Right-side fields must be vertically aligned
Left text must remain left-aligned

goal
The label should communicate:

High quality / premium honey
Regional trust and authenticity
Clean and professional print-ready design

Reference
A reference image is provided showing:

exact placement of all fields
general layout structure

⚠️ The reference is for layout guidance only — not for copying design style.
Updates

All mandatory information must be in German like the address
Bottling point:
Lutz Pfeiffer Beekeeping
Obere Lindmarkw. 17
08437 Wabental
Tel.: 04521 5522417
www.wabenhaus-laden.de

Target Market(s)

Germany

Font styles to use
Sans Serif
Other font styles liked:
• Montserrat, Open Sans, Libre Baskerville

Colors
00AB8E
00BBA5
67D7C9
C6EFE9
E9F9F6
59FF00
82FF00
B8FF75
E3FFCB
F4FFEA
FFF300
FFF600
FEFA6F
FFFEC7
FFFEE8
FFC000
F8CF3A
FAE287
FDF2CF
FEFAEE
F0912C
F2A743
F7CA91
FBE8D2
FDF5EE
EE7325
F08F49
F5BC92
FAE3D3
FDF4ED

Requirements
Must have
• Mandatory Information on Honey Labels (Germany / EU) (Product Name, Country of origin, Net quantity, Minimum durability date (placeholder), Name and address of the food business operator, Batch / lot identification (placeholder), Special warning for infants “Not suitable for infants under 12 months”

```html
<!DOCTYPE html>
<html lang="de">
<head>
<meta charset="utf-8">
<title>German Honey – Label 145 × 55 mm</title>
<link rel="stylesheet" href="https://fonts.googleapis.com/css2?family=Montserrat:wght@500;600&family=Source+Sans+3:wght@400;600;700&display=swap">
<style>
  :root {
    --page: #ffffff;
    --label-cream: #fcf5e3;
    --meadow-tone: #efe2c8;
    --copper-dark: #9a5a3a;
    --copper-light: #e9a27a;
    --hex-fill: #f6ead0;
    --brown-text: #7a4f35;
    --ink: #3a2c22;
    --grey-text: #3f3f42;
    --field-white: #ffffff;
  }
  * { margin: 0; padding: 0; box-sizing: border-box; }
  html, body {
    width: 1200px; height: 1200px; overflow: hidden;
    background: var(--page);
  }
  .label {
    position: absolute;
    left: 50px; top: 391px;
    width: 1100px; height: 418px;
    background: var(--label-cream);
    overflow: hidden;
    font-family: "Source Sans 3", sans-serif;
  }
  .copper-band {
    position: absolute; left: 0; width: 100%; height: 7px;
    background: linear-gradient(90deg, var(--copper-dark), var(--copper-light) 30%, var(--copper-dark) 55%, var(--copper-light) 80%, var(--copper-dark));
    z-index: 3;
  }
  .copper-band.top { top: 0; }
  .copper-band.bottom { bottom: 0; }
  .meadow-backdrop {
    position: absolute; left: 0; right: 0; bottom: 0; height: 260px;
    background: linear-gradient(180deg, rgba(239,226,200,0) 0%, rgba(239,226,200,0.7) 45%, var(--meadow-tone) 100%);
    z-index: 0;
  }
  .bottler {
    position: absolute; left: 34px; top: 33px;
    color: var(--brown-text);
    font-size: 18px; line-height: 27.8px; font-style: normal;
    z-index: 2;
  }
  .bottler .strong { font-weight: 700; }
  .hexagon {
    position: absolute; left: 445px; top: 30px;
    width: 210px; height: 242px;
    z-index: 2;
  }
  .hex-content {
    position: absolute; left: 445px; top: 30px; width: 210px; height: 242px;
    z-index: 2; text-align: center; color: var(--ink);
    font-family: "Montserrat", sans-serif;
  }
  .product-name {
    position: absolute; left: 0; right: 0; top: 78px;
    font-size: 27px; font-weight: 600; line-height: 36px;
    letter-spacing: 3px; padding-left: 3px;
  }
  .divider {
    position: absolute; left: 80px; top: 160px; width: 50px; height: 2px;
    background: var(--copper-dark);
  }
  .net-weight {
    position: absolute; left: 0; right: 0; top: 172px;
    font-size: 17px; font-weight: 500; line-height: 22px;
    letter-spacing: 1px; color: var(--brown-text);
  }
  .field {
    position: absolute; width: 211px; height: 90px;
    background: var(--field-white); border-radius: 12px;
    z-index: 2;
  }
  .field.variety { left: 444px; top: 298px; }
  .field.best-before { left: 853px; top: 71px; }
  .field.lot { left: 853px; top: 216px; }
  .field-caption {
    position: absolute; left: 852px;
    font-size: 16.5px; line-height: 20px; color: var(--grey-text);
    z-index: 2;
  }
  .field-caption.best-before { top: 44px; }
  .field-caption.lot { top: 188px; }
</style>
</head>
<body>
  <main class="label">
    <div class="copper-band top"></div>
    <div class="meadow-backdrop" role="img" aria-label="Soft fine-line sketch of a wildflower meadow in front of a misty forest"></div>

    <address class="bottler">
      <div class="strong">Bottling point:</div>
      <div class="strong">Lutz Pfeiffer Beekeeping</div>
      <div>Obere Lindmarkweg 17</div>
      <div>08437 Wabental</div>
      <div>Tel.: 04521 5522417</div>
      <div>mail@wabenhaus-laden.de</div>
    </address>

    <svg class="hexagon" viewBox="0 0 210 242" aria-hidden="true">
      <polygon points="105,3 207,62 207,180 105,239 3,180 3,62"
               fill="#f6ead0" stroke="#b0714c" stroke-width="2"/>
      <polygon points="105,12 199,67 199,175 105,230 11,175 11,67"
               fill="none" stroke="#d9a07c" stroke-width="1"/>
    </svg>

    <div class="hex-content">
      <h1 class="product-name">GERMAN<br>HONEY</h1>
      <div class="divider"></div>
      <div class="net-weight">500 g</div>
    </div>

    <div class="field variety"></div>

    <div class="field-caption best-before">Best before</div>
    <div class="field best-before"></div>
    <div class="field-caption lot">Lot number</div>
    <div class="field lot"></div>

    <div class="copper-band bottom"></div>
  </main>
</body>
</html>
```